professional business card

A Clean looking business card for a money transfer company. Our company is call Velorix= Transfer + Send = Transcend (next level)
to show professionalism as well as some effects to show digital tech.

1 side to have position, name and address
2 side to have company name and show that we provide money exchange and cross-border money transfer

Target Market(s)

Remittance companies and high net worth individuals

Industry/Entity Type

Finance

Contact Information for Business Card

Name, address, email, title, services- money exchange and cross-border remittance

Requirements
Nice to have
• Digital age feel

```html
<!DOCTYPE html>
<html lang="en">
<head>
<meta charset="utf-8">
<title>Velorix Business Card</title>
<link rel="stylesheet" href="https://fonts.googleapis.com/css2?family=Montserrat:wght@400;500;600;700&display=swap">
<style>
  :root {
    --backdrop: #7f98bb;
    --card-light: #ffffff;
    --card-dark: #2a3642;
    --ink: #27323f;
    --ink-soft: #4a5563;
    --accent: #6cc8d6;
    --on-dark: #f2f5f8;
    --divider: #5b6470;
  }
  * { box-sizing: border-box; margin: 0; padding: 0; }
  html, body {
    width: 1200px; height: 876px; overflow: hidden;
    background: var(--backdrop);
    font-family: "Montserrat", sans-serif;
  }
  .stage {
    width: 1200px; height: 876px;
    display: flex; align-items: center; justify-content: center; gap: 40px;
  }
  .card {
    width: 540px; height: 309px; position: relative;
    box-shadow: 0 10px 28px rgba(30, 45, 70, 0.28);
  }
  /* Front */
  .card--front { background: var(--card-light); color: var(--ink); }
  .person {
    position: absolute; top: 34px; left: 262px; text-align: center;
  }
  .person__name { font-weight: 700; font-size: 16px; letter-spacing: 0.5px; text-transform: uppercase; }
  .person__title { color: var(--accent); font-size: 14px; margin-top: 2px; }
  .brand {
    position: absolute; top: 96px; left: 0; width: 100%;
    display: flex; align-items: center; justify-content: center; gap: 14px;
  }
  .brand__dot { width: 34px; height: 34px; border-radius: 50%; background: var(--accent); }
  .brand__name { font-weight: 600; font-size: 50px; letter-spacing: 1px; color: var(--ink); text-transform: uppercase; }
  .tagline {
    position: absolute; top: 166px; width: 100%; text-align: center;
    font-size: 14px; color: var(--ink-soft);
  }
  .contacts {
    position: absolute; bottom: 28px; left: 24px; right: 24px;
    display: flex; justify-content: space-between; align-items: flex-end;
  }
  .contact { flex: 1; text-align: center; font-size: 13px; color: var(--ink-soft); line-height: 1.35; }
  .contact__icon { display: block; margin: 0 auto 8px; width: 18px; height: 18px; }
  .contact-divider { width: 1px; height: 40px; background: var(--divider); }
  /* Back */
  .card--back {
    background: linear-gradient(135deg, #33404d 0%, var(--card-dark) 55%, #222c36 100%);
    color: var(--on-dark);
    display: flex; flex-direction: column; align-items: center; justify-content: center;
  }
  .card--back .brand { position: static; }
  .card--back .brand__name { color: var(--on-dark); font-size: 48px; }
  .services {
    margin-top: 14px; text-align: center; text-transform: uppercase;
    font-size: 13px; letter-spacing: 1px; line-height: 1.35; font-weight: 500;
  }
  .website {
    margin-top: 26px; font-size: 14px; letter-spacing: 9px; color: #b9c2cc;
  }
</style>
</head>
<body>
<main class="stage">
  <section class="card card--front">
    <div class="person">
      <p class="person__name">Darin Kessler</p>
      <p class="person__title">Director</p>
    </div>
    <div class="brand">
      <span class="brand__dot"></span>
      <span class="brand__name">Velorix</span>
    </div>
    <p class="tagline">Money exchange and cross-border remittance</p>
    <div class="contacts">
      <div class="contact">
        <svg class="contact__icon" viewBox="0 0 18 18" aria-hidden="true">
          <circle cx="9" cy="9" r="9" fill="#6cc8d6"/>
          <rect x="6" y="4" width="6" height="10" rx="1" fill="#fff"/>
          <rect x="7" y="5.3" width="4" height="6.5" fill="#6cc8d6"/>
        </svg>
        +000 12345 6789
      </div>
      <span class="contact-divider"></span>
      <div class="contact">
        <svg class="contact__icon" viewBox="0 0 18 18" aria-hidden="true">
          <circle cx="9" cy="9" r="9" fill="#6cc8d6"/>
          <path d="M9 4a3.2 3.2 0 0 0-3.2 3.2C5.8 9.8 9 14 9 14s3.2-4.2 3.2-6.8A3.2 3.2 0 0 0 9 4z" fill="#fff"/>
          <circle cx="9" cy="7.2" r="1.2" fill="#6cc8d6"/>
        </svg>
        Street Address Here<br>Singapore, 2222
      </div>
      <span class="contact-divider"></span>
      <div class="contact">
        <svg class="contact__icon" viewBox="0 0 18 18" aria-hidden="true">
          <circle cx="9" cy="9" r="9" fill="#6cc8d6"/>
          <rect x="4.5" y="5.8" width="9" height="6.4" rx="0.6" fill="#fff"/>
          <path d="M4.8 6.2 9 9.4l4.2-3.2" fill="none" stroke="#6cc8d6" stroke-width="0.9"/>
        </svg>
        urname@email.com
      </div>
    </div>
  </section>

  <section class="card card--back">
    <div class="brand">
      <span class="brand__dot"></span>
      <span class="brand__name">Velorix</span>
    </div>
    <p class="services">We provide money exchange<br>and cross-border money transfer</p>
    <p class="website">www.velorix.com</p>
  </section>
</main>
</body>
</html>
```